Veridan Crest Business Cards

Veridan Crest Prestige Portfolio Group is a global representation business focusing on high end luxury. We need business cards to epitomize our global, luxury delivery model.

Target Market(s)

Global Representation in the hospitality industry

Industry/Entity Type

Hospitality

Contact Information for Business Card

name
title
email: first.last@vc-ppg.com
web: www.vc-ppg.com
mobile:

Requirements
Must have
• double sided design
• incorporate logo colours
• have logo prominent
Should not have
• no designs not incorporating logo colours.

```html
<!DOCTYPE html>
<html lang="en">
<head>
<meta charset="utf-8">
<title>Veridan Crest Business Cards</title>
<link rel="stylesheet" href="https://fonts.googleapis.com/css2?family=Cinzel:wght@400;500&family=Open+Sans:wght@400&display=swap">
<style>
  :root {
    --backdrop: #2c2c2a;
    --card-black: #0d0d0d;
    --pattern-black: #131313;
    --gold: #c2a978;
    --gold-deep: #a48a5c;
    --ink-light: #e6e2da;
  }
  * { margin: 0; padding: 0; box-sizing: border-box; }
  html, body {
    width: 1200px;
    height: 824px;
    overflow: hidden;
    background: var(--backdrop);
  }
  .sheet {
    position: relative;
    width: 1200px;
    height: 824px;
  }
  .card {
    position: absolute;
    top: 262px;
    width: 525px;
    height: 300px;
    background: var(--card-black);
    border-radius: 4px;
    box-shadow: 0 14px 30px rgba(0, 0, 0, 0.55);
    overflow: hidden;
  }
  .card--front { left: 50px; }
  .card--back { left: 625px; }

  .monogram-field {
    position: absolute;
    inset: 0;
    background: linear-gradient(135deg, var(--pattern-black), var(--card-black) 70%);
  }

  .brand-lockup {
    position: absolute;
    display: flex;
    flex-direction: column;
    align-items: center;
    font-family: "Cinzel", serif;
    font-weight: 500;
    color: var(--gold);
    text-align: center;
  }
  .card--front .brand-lockup {
    left: 0;
    right: 0;
    top: 92px;
  }
  .brand-mark {
    width: 18px;
    height: 18px;
    border-radius: 50%;
    background: var(--gold);
    margin-bottom: 14px;
  }
  .brand-name {
    font-size: 40px;
    letter-spacing: 2px;
    line-height: 1.1;
  }
  .brand-group {
    font-size: 13px;
    letter-spacing: 2.5px;
    margin-top: 8px;
  }

  .card--back .brand-lockup {
    left: 36px;
    top: 112px;
    width: 200px;
  }
  .card--back .brand-mark {
    width: 12px;
    height: 12px;
    margin-bottom: 10px;
  }
  .card--back .brand-name {
    font-size: 25px;
    letter-spacing: 1px;
  }
  .card--back .brand-group {
    font-size: 8px;
    letter-spacing: 1.5px;
    margin-top: 6px;
  }

  .holder {
    position: absolute;
    left: 268px;
    top: 104px;
  }
  .holder-name {
    font-family: "Cinzel", serif;
    font-weight: 400;
    font-size: 20px;
    letter-spacing: 1.5px;
    color: var(--ink-light);
  }
  .holder-title {
    font-family: "Cinzel", serif;
    font-size: 12px;
    letter-spacing: 1.5px;
    color: var(--gold-deep);
    margin-top: 2px;
  }
  .contact-list {
    list-style: none;
    margin-top: 22px;
    font-family: "Open Sans", sans-serif;
    font-size: 12px;
    color: var(--ink-light);
  }
  .contact-item {
    display: flex;
    align-items: center;
    gap: 8px;
    height: 19px;
  }
  .contact-icon {
    width: 11px;
    height: 11px;
    flex: none;
  }
</style>
</head>
<body>
<main class="sheet">

  <section class="card card--front" aria-label="Card front">
    <div class="monogram-field" role="img" aria-label="Faint tonal monogram pattern across the card face"></div>
    <div class="brand-lockup">
      <span class="brand-mark"></span>
      <span class="brand-name">VERIDAN CREST</span>
      <span class="brand-group">PRESTIGE PORTFOLIO GROUP</span>
    </div>
  </section>

  <section class="card card--back" aria-label="Card back">
    <div class="brand-lockup">
      <span class="brand-mark"></span>
      <span class="brand-name">VERIDAN CREST</span>
      <span class="brand-group">PRESTIGE PORTFOLIO GROUP</span>
    </div>

    <div class="holder">
      <p class="holder-name">YOUR NAME</p>
      <p class="holder-title">JOB TITLE</p>
      <ul class="contact-list">
        <li class="contact-item">
          <svg class="contact-icon" viewBox="0 0 12 12" aria-hidden="true">
            <rect x="3" y="0.5" width="6" height="11" rx="1" fill="none" stroke="var(--gold)" stroke-width="1"/>
            <circle cx="6" cy="9.5" r="0.7" fill="var(--gold)"/>
          </svg>
          <span>000 000 0000</span>
        </li>
        <li class="contact-item">
          <svg class="contact-icon" viewBox="0 0 12 12" aria-hidden="true">
            <rect x="0.5" y="2.5" width="11" height="7" fill="none" stroke="var(--gold)" stroke-width="1"/>
            <path d="M0.5 2.5 L6 7 L11.5 2.5" fill="none" stroke="var(--gold)" stroke-width="1"/>
          </svg>
          <span>first.last@vc-ppg.com</span>
        </li>
        <li class="contact-item">
          <svg class="contact-icon" viewBox="0 0 12 12" aria-hidden="true">
            <circle cx="6" cy="6" r="5.2" fill="none" stroke="var(--gold)" stroke-width="1"/>
            <ellipse cx="6" cy="6" rx="2.3" ry="5.2" fill="none" stroke="var(--gold)" stroke-width="0.8"/>
            <path d="M0.8 6 H11.2" stroke="var(--gold)" stroke-width="0.8"/>
          </svg>
          <span>www.vc-ppg.com</span>
        </li>
      </ul>
    </div>
  </section>

</main>
</body>
</html>
```